Buchcover-Design für Detoxkur
Vielen lieben Dank für die professionelle Zusammenarbeit, die sich auch im zweiten Projekt erfolgreich bestätigen ließ. Tip Top! Dankeschön!!!!
Zielgruppe
Ich bin Gesundheits- und Ernährungsberater und suche nach einem Buchcover für mein neues Projekt (Taschenbuch und E-Book) Meine Zielgruppe sind Menschen die auf der Suche nach Heilung und mehr Wohlbefinden sind. (Detoxkur-Entschlacken und Entgiften etc....)
Aufgabenstellung
Das Design sollte durch den Titel deutlich auffallen. Vorzugsweise ein dunkler Hintergrund, Titel in großer Schrift. Eingearbeitet etwas Gemüse und Obst, grüner Saft oder auch ein Smoothie, Zitronenwasser, Magen- und Darmtrakt oder ähnlichem. Es darf auch verspielt sein aber dennoch Niveauvoll.
Das Buch einschließlich Titel und Untertitel, sowie Klappentext werden derzeit von einem Lektor bearbeitet, also können diesbezüglich noch leichte Änderungen anfallen die dann anzupassen wären.
Das Buchformat ist 12cm x 19cm. Die Endgültigen Abmaße müssten nach dem Buchindesign noch angepasst werden, wenn die Seitenzahlen feststehen.
Würde gerne den Coverdesigner im Impressum des Buchs erwähnen und Bitte darum um Einverständnis, wenn es auch erwünscht sein sollte!
Derzeitiger Text :
Titel: Morgenlicht - Finde Ruhe durch Wandern und Tagträumen
Untertitel: - Durch Entgiften und Entschlacken das Wohlbefinden steigern, die Darmgesundheit wieder herstellen, das Gewicht reduzieren und die Heilung für Körper und Geist einleiten -
Klappentext: Bist du auf der Suche nach mehr Wohlbefinden und möchtest deine Gesundheit nachhaltig verbessern? Suchst du nach Methoden deinen Körper von Schadstoffen zu befreien, die dich in der Vergangenheit belastet haben? Möglicherweise fragst du dich warum das so ist und was es damit auf sich hat?
Detox, Entschlacken und Entgiften, Diäten und eine gesündere Ernährungsweise ist in aller Munde. Der Grund dafür ist bei zahlreichen Menschen ein mangelndes Wohlbefinden durch zivillisationsbedingte Einflüsse wie Umweltverschmutzungen, Stress und eine unbewusste Ernährungsweise. Diese Faktoren führen zu krankhaften Symptomen, Energie- und Antriebslosigkeit und letztendlich zu den steigenden Zahlen übergewichtiger Menschen in unserer Bevölkerung.
In diesem Ratgeber erfährst du, wie wichtig es ist sich zu entgiften und wie wichtig dafür eine gesunde Ernähru..

```html
<!DOCTYPE html>
<html lang="de">
<head>
<meta charset="utf-8">
<title>Morgenlicht – Buchcover</title>
<link href="https://fonts.googleapis.com/css2?family=Alfa+Slab+One&family=Didact+Gothic&display=swap" rel="stylesheet">
<style>
  :root {
    --stage: #e9e9ea;
    --slate-dark: #141414;
    --slate-mid: #2c2c2c;
    --slate-light: #3a3a3a;
    --leaf-green: #5bb431;
    --kale-dark: #2f4a1c;
    --juice-mid: #6f9a3e;
    --apple-cream: #e8e4c8;
    --paper-white: #ffffff;
    --portrait-blue: #4b6a93;
    --portrait-grey: #c9c6c1;
  }
  * { box-sizing: border-box; margin: 0; padding: 0; }
  html, body { width: 1200px; height: 802px; overflow: hidden; background: var(--stage); }
  body { position: relative; font-family: "Didact Gothic", sans-serif; color: var(--paper-white); }

  .cover {
    position: absolute; top: 45px; width: 450px; height: 712px;
    background:
      radial-gradient(ellipse at 30% 40%, var(--slate-light) 0%, transparent 60%),
      radial-gradient(ellipse at 75% 75%, var(--slate-mid) 0%, transparent 55%),
      var(--slate-dark);
    box-shadow: 0 10px 28px rgba(0,0,0,.25);
  }
  .cover--front { left: 60px; }
  .cover--back { left: 640px; }

  .front__title {
    position: absolute; top: 62px; left: 0; width: 100%;
    text-align: center; font-family: "Alfa Slab One", serif;
    font-size: 60px; line-height: 1; color: var(--leaf-green); letter-spacing: -1px;
  }
  .front__subtitle {
    position: absolute; top: 134px; right: 42px;
    font-size: 13px; letter-spacing: .2px;
  }
  .front__photo {
    position: absolute; top: 172px; left: 0; width: 400px; height: 392px;
    border-radius: 0 196px 196px 0;
    background:
      radial-gradient(ellipse at 68% 30%, var(--apple-cream) 0%, transparent 42%),
      radial-gradient(ellipse at 80% 75%, var(--kale-dark) 0%, transparent 50%),
      linear-gradient(135deg, #8fb35e 0%, var(--juice-mid) 50%, var(--kale-dark) 100%);
  }

  .front__author {
    position: absolute; top: 582px; right: 28px; text-align: right; line-height: 1.05;
  }
  .front__author-name { font-size: 20px; letter-spacing: .5px; }
  .front__author-role { font-size: 14px; color: var(--leaf-green); }
  .front__claim {
    position: absolute; top: 634px; left: 16px; right: 28px;
    font-size: 11px; line-height: 1.35; text-align: justify; text-align-last: right;
  }

  .back__portrait {
    position: absolute; top: 125px; left: 28px; width: 112px; height: 152px;
    background: linear-gradient(160deg, var(--portrait-grey) 0%, #a8a59f 45%, var(--portrait-blue) 100%);
  }
  .back__panel {
    position: absolute; top: 125px; left: 140px; width: 246px; height: 152px;
    background: var(--leaf-green);
  }
  .back__panel-lower {
    position: absolute; top: 277px; left: 80px; width: 306px; height: 340px;
    background: var(--leaf-green);
  }
  .back__blurb-intro {
    position: absolute; top: 140px; left: 152px; width: 222px;
    font-size: 10.5px; line-height: 1.42; text-align: justify;
  }
  .back__blurb {
    position: absolute; top: 290px; left: 92px; width: 282px;
    font-size: 10px; line-height: 1.4; text-align: justify;
  }
  .back__blurb p + p { margin-top: 10px; }
  .back__signature {
    position: absolute; top: 580px; right: 78px; font-size: 16px; letter-spacing: 1px;
  }

  .spine {
    position: absolute; top: 45px; left: 1090px; width: 40px; height: 712px;
    background: var(--leaf-green); box-shadow: 0 10px 28px rgba(0,0,0,.2);
  }
  .spine__text {
    position: absolute; left: 50%; top: 50%;
    transform: translate(-50%, -50%) rotate(-90deg);
    white-space: nowrap; display: flex; align-items: center; gap: 18px;
  }
  .spine__title { font-family: "Alfa Slab One", serif; font-size: 22px; }
  .spine__subtitle { font-size: 11px; letter-spacing: .8px; }
  .spine__author { font-size: 9px; line-height: 1.1; }
</style>
</head>
<body>

<section class="cover cover--front">
  <h1 class="front__title">Morgenlicht</h1>
  <p class="front__subtitle">Finde Ruhe durch Wandern und Tagträumen</p>

  <div class="front__photo" role="img" aria-label="Foto in Magenform mit weißem Rand: grüner Saft im Glas, Apfelhälften, Limette und Grünkohl"></div>

  <div class="front__author">
    <div class="front__author-name">Jonas Kerbel</div>
    <div class="front__author-role">Gesundheits- und Ernährungsberater</div>
  </div>
  <p class="front__claim">Durch Entgiften und Entschlacken das Wohlbefinden steigern, die Darmgesundheit wieder herstellen, das Gewicht reduzieren und die Heilung für Körper und Geist einleiten.</p>
</section>

<section class="cover cover--back">
  <div class="back__portrait" role="img" aria-label="Porträtfoto des Autors im blauen Hemd"></div>
  <div class="back__panel"></div>
  <div class="back__panel-lower"></div>

  <p class="back__blurb-intro">Bist du auf der Suche nach mehr Wohlbefinden und möchtest deine Gesundheit nachhaltig verbessern? Suchst du nach Methoden deinen Körper von Schadstoffen zu befreien, die dich in der Vergangenheit belastet haben? Möglicherweise fragst du dich warum das so ist und was es damit auf sich hat?</p>

  <div class="back__blurb">
    <p>Detox, Entschlacken und Entgiften, Diäten und eine gesündere Ernährungsweise ist in aller Munde. Der Grund dafür ist bei zahlreichen Menschen ein mangelndes Wohlbefinden durch zivilisationsbedingte Einflüsse wie Umweltverschmutzungen, Stress und eine unbewusste Ernährungsweise. Diese Faktoren führen zu krankhaften Symptomen, Energie- und Antriebslosigkeit und letztendlich zu den steigenden Zahlen übergewichtiger Menschen in unserer Bevölkerung.</p>
    <p>In diesem Ratgeber erfährst du, wie wichtig es ist sich zu entgiften und wie wichtig dafür eine gesunde Ernährungsweise ist. Zusätzlich erfährst du, wie du praktische Heilmethoden anwendest, die die Darmgesundheit wiederherstellen und wie du die Entgiftung in den einzelnen Bereichen des Körpers vorantreibst. Denn Detox ist heutzutage wichtiger denn je!</p>
  </div>

  <p class="back__signature">Jonas Kerbel</p>
</section>

<aside class="spine">
  <div class="spine__text">
    <span class="spine__author">Jonas Kerbel</span>
    <span class="spine__title">Morgenlicht</span>
    <span class="spine__subtitle">Finde Ruhe durch Wandern und Tagträumen</span>
  </div>
</aside>

</body>
</html>
```